Ground breaking athletic gear company needs a kick ass business card

We are an American start up athletic gear company that uses a medically proven biohack to boost athletic performance. Heat kills strength and endurance. Our gear helps athletes manage heat better and ultimatley can improve them by up to 10% instantly. Nothing like it out there! Launching this summer.
We are looking for a modern, minimalist design that captures a sporty edge. Check out www.vanteluxgear.com, @vanteluxgear on pictorama for more ideas.

Target Market(s)

25-35 year olds, male and female athletes, vortexlift athletes, competitive runners

Industry/Entity Type

Business

Contact Information for Business Card

Derek Hollins
Founder
derekh@vanteluxgear.com
www.VanteluxGear.com
+1 (555) 014-2286

Font styles to use
Sans Serif

Requirements
Must have
• Logo and icon
• All contact information
• derekh@vanteluxgear.com
• +1 (555) 019-4431 M
• +1 (555) 014-2286
Nice to have
• Tag line : "Cool & Conquer"

```html
<!DOCTYPE html>
<html lang="en">
<head>
<meta charset="utf-8">
<title>Vantelux Gear — Business Card</title>
<link rel="stylesheet" href="https://fonts.googleapis.com/css2?family=Exo+2:wght@300;400;600&display=swap">
<style>
  :root {
    --stage: #182c3a;
    --sky: #87cdf9;
    --paper: #ffffff;
    --ink: #111111;
    --grey: #808080;
    --label: #555555;
  }
  html, body {
    margin: 0;
    width: 1200px;
    height: 1200px;
    overflow: hidden;
    background: var(--stage);
    font-family: "Exo 2", sans-serif;
  }
  .canvas { position: relative; width: 1200px; height: 1200px; }
  .card {
    position: absolute;
    left: 215px;
    width: 770px;
    height: 427px;
    background: var(--sky);
    overflow: hidden;
  }
  .card--front { top: 100px; }
  .card--back { top: 652px; }
  .card svg.art { position: absolute; inset: 0; }

  .holder-name {
    position: absolute;
    left: 93px;
    top: 92px;
    margin: 0;
    font-size: 40px;
    font-weight: 600;
    color: var(--sky);
    letter-spacing: -0.3px;
  }
  .holder-role {
    position: absolute;
    left: 93px;
    top: 145px;
    margin: 0;
    font-size: 20px;
    font-weight: 300;
    color: var(--label);
  }
  .contact-list {
    position: absolute;
    left: 128px;
    top: 224px;
    margin: 0;
    padding: 0;
    list-style: none;
  }
  .contact-item {
    display: flex;
    align-items: center;
    height: 24px;
    margin-bottom: 14px;
    font-size: 14px;
    font-weight: 400;
    color: var(--sky);
    letter-spacing: -0.2px;
  }
  .contact-item svg { width: 24px; height: 24px; margin-right: 23px; }

  .brand-name {
    position: absolute;
    left: 285px;
    width: 200px;
    top: 200px;
    margin: 0;
    text-align: center;
    font-size: 19px;
    line-height: 24px;
    font-weight: 400;
    letter-spacing: 2.5px;
    white-space: nowrap;
    color: var(--ink);
  }
  .back-url {
    position: absolute;
    left: 0;
    width: 770px;
    top: 393px;
    text-align: center;
    font-size: 16px;
    font-weight: 300;
    color: var(--paper);
  }
</style>
</head>
<body>
<main class="canvas">

  <section class="card card--front">
    <svg class="art" width="770" height="427" viewBox="0 0 770 427">
      <path class="wave-white" fill="var(--paper)"
        d="M0,120 C60,60 150,30 260,25 C430,20 520,70 770,72 L770,285 C600,310 420,400 250,400 C140,400 60,380 0,360 Z"/>
      <path class="swoosh-top" fill="var(--grey)"
        d="M0,95 C50,60 110,38 170,31 C110,45 50,78 0,113 Z"/>
      <path class="swoosh-bottom" fill="var(--grey)"
        d="M0,342 C50,370 110,390 170,395 C110,393 50,378 0,362 Z"/>
      <g class="rule" stroke="var(--sky)" stroke-width="1">
        <line x1="0" y1="189.5" x2="457" y2="189.5"/>
        <line x1="600" y1="189.5" x2="630" y2="189.5"/>
        <line x1="722" y1="189.5" x2="770" y2="189.5"/>
      </g>
      <rect class="athlete-figure" role="img" aria-label="Silhouette of an athlete holding a ball overhead"
        x="498" y="153" width="272" height="160" rx="60" fill="var(--sky)"/>
    </svg>

    <h1 class="holder-name">Derek Hollins</h1>
    <p class="holder-role">Founder</p>

    <ul class="contact-list">
      <li class="contact-item">
        <svg viewBox="0 0 24 24" aria-hidden="true"><path fill="var(--grey)" d="M6.6 3.5c.6-.4 1.3-.3 1.7.3l2 3c.4.6.3 1.3-.2 1.7L9 9.5c.9 2.2 2.7 4.2 5 5.3l1-1.1c.5-.5 1.2-.5 1.7-.1l2.9 2.2c.5.4.6 1.2.2 1.7l-1.3 1.6c-.7.8-1.800 1.1-2.8.7C9.8 17.9 5.9 13.7 4.5 8.3c-.3-1 .1-2.1.9-2.7z"/></svg>
        (555) 014-2286
      </li>
      <li class="contact-item">
        <svg viewBox="0 0 24 24" aria-hidden="true"><rect x="2" y="6" width="20" height="13" fill="var(--grey)"/><path d="M2 6 L12 14 L22 6 M2 19 L9 12 M22 19 L15 12" stroke="var(--paper)" stroke-width="1.3" fill="none"/></svg>
        derekh@vanteluxgear.com
      </li>
      <li class="contact-item">
        <svg viewBox="0 0 24 24" aria-hidden="true"><circle cx="12" cy="12" r="9.5" fill="var(--grey)"/><g stroke="var(--paper)" stroke-width="1.3" fill="none"><ellipse cx="12" cy="12" rx="4" ry="9.5"/><line x1="2.5" y1="12" x2="21.5" y2="12"/></g></svg>
        www.VanteluxGear.com
      </li>
    </ul>
  </section>

  <section class="card card--back">
    <svg class="art" width="770" height="427" viewBox="0 0 770 427">
      <g class="rule" stroke="var(--paper)" stroke-width="1.5">
        <line x1="0" y1="212" x2="272" y2="212"/>
        <line x1="498" y1="212" x2="770" y2="212"/>
      </g>
    </svg>
    <p class="brand-name">VANTELUX GEAR</p>
    <div class="back-url">www.vanteluxgear.com</div>
  </section>

</main>
</body>
</html>
```